Custom Manufacturing Company square space website design

I own a custom manufacturing company that uses precision cutting technology to manufacture project components over a couple industries. We have an industrial CNC router and state of the art edge bander and cut a lot of cabinetry components for cabinet shops, builders, closet companies, ect. We offer design and assembly for any cabinetry or can build cabinets to spec. We also cut components for other industries out of wood, plastics, acryclics, ect. We offer design engineering services, product development protype services. we have a 3D printer farm. We want our communicate trust, dependability, and the value we place on client relationships.

We essentially want a credibility website. Landing page and drops downs for services we offer, capabilites, about us, contact

```html
<!DOCTYPE html>
<html lang="en">
<head>
<meta charset="utf-8">
<title>North Ridge CNC — Precision Cutting Technology</title>
<link rel="stylesheet" href="https://fonts.googleapis.com/css2?family=Montserrat:wght@600;700;800;900&family=Roboto:wght@400;500;700&display=swap">
<style>
:root{
  --ink:#111111;
  --dark:#1a1a1a;
  --darker:#0e0e0e;
  --muted:#555555;
  --light:#f2f2f2;
  --mid:#dcdcdc;
  --white:#ffffff;
  --accent:#2a7fd4;
  --steel:#3c5a7c;
  --wood:#8a5a36;
  --copper:#a8673a;
}
*{box-sizing:border-box;margin:0;padding:0}
html,body{width:1200px;height:4640px;overflow:hidden}
body{font-family:"Roboto",Arial,sans-serif;color:var(--ink);background:var(--white);position:relative}
.heading{font-family:"Montserrat",Arial,sans-serif;font-weight:900;text-transform:uppercase;letter-spacing:1px}
.section-title{text-align:center;font-size:32px;position:absolute;left:0;width:1200px}
.section-title::after{content:"";display:block;width:150px;height:4px;background:var(--ink);margin:10px auto 0}
.lead{position:absolute;left:300px;width:600px;text-align:center;font-size:14px;line-height:20px;color:var(--muted)}
.photo{position:absolute;overflow:hidden}
.brand{display:flex;align-items:center;gap:10px;font-family:"Montserrat",Arial,sans-serif;font-weight:800;font-size:16px;letter-spacing:1px}
.brand-mark{width:18px;height:18px;border:2px solid currentColor}

/* header */
.site-header{position:absolute;top:0;left:0;width:1200px;height:120px;background:var(--white);display:flex;align-items:center;padding:0 100px 0 110px}
.site-header .brand{color:var(--ink)}
.main-nav{display:flex;gap:36px;margin-left:auto;font-size:14px;font-weight:700;text-transform:uppercase}
.main-nav span.drop::after{content:" ▾";font-size:11px}
.call{display:flex;align-items:center;gap:10px;font-weight:700;font-size:20px;position:absolute;right:130px;top:8px}
.call-icon{width:30px;height:30px;background:var(--ink);display:flex;align-items:center;justify-content:center}
.main-nav{margin-top:50px}

/* hero */
.hero{position:absolute;top:120px;left:0;width:1200px;height:520px;background:linear-gradient(110deg,#0b1420 0%,#1c2c42 45%,#3a4e6a 70%,#b57a3a 88%,#1a2434 100%)}
.hero-title{position:absolute;left:128px;top:160px;color:var(--white);font-size:46px;line-height:52px;letter-spacing:4px}
.hero-sub{position:absolute;left:128px;top:322px;color:var(--white);font-size:22px;font-weight:500}

/* welcome */
.welcome{position:absolute;top:640px;left:0;width:1200px;height:980px;background:linear-gradient(#ffffff 0%,#ffffff 55%,#e6e6e6 100%)}
.tile{position:absolute;display:flex;align-items:center;justify-content:center;color:var(--white);font-family:"Montserrat",Arial,sans-serif;font-weight:800;font-size:20px;text-transform:uppercase}
.btn{position:absolute;background:var(--ink);color:var(--white);font-size:13px;font-weight:700;text-transform:uppercase;display:flex;align-items:center;justify-content:center}

/* services */
.services{position:absolute;top:1620px;left:0;width:1200px;height:860px;background:linear-gradient(#f4f4f4,#ffffff 40%)}
.tabs{position:absolute;top:228px;left:300px;width:600px;display:flex;justify-content:space-between;font-size:14px;text-align:center;line-height:18px;border-bottom:1px solid var(--mid)}
.tab{padding-bottom:10px;width:180px}
.tab.active{color:var(--accent);border-bottom:3px solid var(--accent)}
.service-panel{left:172px;top:320px;width:856px;height:468px;background:linear-gradient(90deg,#5a3e28,#8a6440 40%,#3a2c22 75%,#2a2420)}
.panel-copy{position:absolute;left:470px;top:100px;width:340px;color:var(--white)}
.panel-copy h3{font-size:26px;line-height:30px}
.panel-copy p{font-size:13px;line-height:17px;margin:12px 0 18px}
.panel-copy .outline{display:inline-block;border:1px solid var(--white);padding:8px 16px;font-size:12px;font-weight:700}

/* why */
.why{position:absolute;top:2480px;left:0;width:1200px;height:720px;background:linear-gradient(#ffffff,#e4e4e4)}
.why-title{position:absolute;left:128px;top:88px;font-size:32px}
.why-lead{position:absolute;left:128px;top:160px;width:470px;font-size:14px;line-height:20px;color:var(--muted)}
.reason{position:absolute;left:128px;display:flex;gap:20px;width:460px}
.reason svg{flex:none}
.reason h4{font-size:20px;font-weight:700;margin-bottom:6px}
.reason p{font-size:13px;line-height:17px;color:var(--muted)}
.framed{border:3px solid var(--ink)}

/* blog */
.blog{position:absolute;top:3200px;left:0;width:1200px;height:640px;background:var(--white)}
.post{position:absolute;top:220px;width:292px;height:340px;background:var(--white);box-shadow:0 2px 10px rgba(0,0,0,.12)}
.post .photo{position:relative;height:188px}
.post p{padding:18px 18px 0;font-size:19px;line-height:23px;color:#666}
.post time{display:block;padding:22px 18px 0;font-size:13px;font-weight:700}

/* contact */
.contact{position:absolute;top:3840px;left:0;width:1200px;height:500px;background:linear-gradient(135deg,#2a2a2a,#151515 60%,#222)}
.contact .section-title{color:var(--white);top:110px}
.contact .section-title::after{background:var(--white)}
.field{position:absolute;background:var(--white);font-size:13px;padding:10px 14px;color:var(--ink)}

/* footer */
.site-footer{position:absolute;top:4340px;left:0;width:1200px;height:300px;background:var(--darker);color:var(--white)}
.info{position:absolute;left:220px;display:flex;gap:22px;font-size:14px;line-height:18px}
.info strong{display:block}
.site-footer .brand{position:absolute;left:540px;top:110px;font-size:18px;color:var(--white)}
.foot-links{position:absolute;left:800px;top:60px;font-size:15px;font-weight:500;line-height:26px}
.copyright{position:absolute;top:218px;left:0;width:1200px;text-align:center;font-size:13px;color:#cfcfcf}
</style>
</head>
<body>

<header class="site-header">
  <div class="brand"><span class="brand-mark"></span>NORTH RIDGE CNC</div>
  <div class="call">
    <span class="call-icon"><svg width="16" height="16" viewBox="0 0 24 24" fill="#fff"><path d="M6.6 10.8a15 15 0 0 0 6.6 6.6l2.2-2.2c.3-.3.7-.4 1-.2 1.1.4 2.3.6 3.6.6.6 0 1 .4 1 1V20c0 .6-.4 1-1 1A17 17 0 0 1 3 4c0-.6.4-1 1-1h3.5c.6 0 1 .4 1 1 0 1.3.2 2.5.6 3.6.1.3 0 .7-.2 1z"/></svg></span>
    CALL: 555 XXX 0142
  </div>
  <nav class="main-nav">
    <span>Home</span><span class="drop">Services We Offer</span><span class="drop">Capabilites</span><span>About Us</span><span>Contact</span>
  </nav>
</header>

<section class="hero" role="img" aria-label="CNC cutting head sending sparks over a machined metal sheet">
  <h1 class="heading hero-title">Precision<br>Cutting<br>Technology</h1>
  <p class="hero-sub">Manufacture proect components</p>
</section>

<section class="welcome">
  <h2 class="heading section-title" style="top:120px">Welcome to North Ridge</h2>
  <p class="lead" style="top:192px">Lorem ipsum dolor sit amet, consectetur adipiscing elit, sed do eiusmod tempor incididunt ut labore et dolore magna aliqua. Quis ipsum suspendisse ultrices gravida. Risus commodo viverra maecenas accumsan lacus vel facilisis.</p>
  <div class="tile" style="left:172px;top:272px;width:260px;height:260px;background:linear-gradient(135deg,#6b4a2e,#a77a4c 60%,#3e2b1c)" role="img" aria-label="CNC router cutting cabinet wood panels">Cabinet Wood</div>
  <div class="tile" style="left:440px;top:272px;width:588px;height:260px;background:linear-gradient(120deg,#2e241c,#6e5038 45%,#9a7a58 70%,#3a3028)" role="img" aria-label="Worker machining a plastic part">Plastics Works</div>
  <div class="tile" style="left:172px;top:540px;width:588px;height:268px;background:linear-gradient(135deg,#1e3048,#4a6a90 50%,#8aa4c4 75%,#2a3c56)" role="img" aria-label="Laser cutting patterned acrylic sheet">Acrylics Works</div>
  <div class="tile" style="left:768px;top:540px;width:260px;height:268px;background:linear-gradient(135deg,#6a4c5a,#a67c8c 55%,#3a2c34)" role="img" aria-label="Close-up of a cutting machine at work">Other Works</div>
  <div class="btn" style="left:512px;top:864px;width:120px;height:40px">Read More</div>
</section>

<section class="services">
  <h2 class="heading section-title" style="top:84px">Our Services</h2>
  <p class="lead" style="top:146px">Lorem ipsum dolor sit amet, consectetur adipiscing elit, sed do eiusmod tempor incididunt ut labore et dolore magna aliqua. Quis ipsum suspendisse ultrices gravida.</p>
  <div class="tabs">
    <div class="tab active">Design Engineering<br>Services</div>
    <div class="tab">Product Development<br>Protype Services</div>
    <div class="tab">3D Printer Farm<br>&nbsp;</div>
  </div>
  <div class="photo service-panel" role="img" aria-label="Craftsman assembling a wooden cabinet in a workshop">
    <div class="panel-copy">
      <h3 class="heading">Design Engineering Services</h3>
      <p>Lorem ipsum dolor sit amet, consectetur adipiscing elit, sed do eiusmod tempor incididunt ut labore et dolore magna aliqua. Quis ipsum suspendisse ultrices gravida. Risus commodo viverra.</p>
      <span class="outline">READ MORE</span>
    </div>
  </div>
</section>

<section class="why">
  <h2 class="heading why-title">Why Choose Us?</h2>
  <p class="why-lead">Lorem ipsum dolor sit amet, consectetur adipiscing elit, sed do eiusmod tempor incididunt ut labore et dolore magna aliqua. Quis ipsum suspendisse ultrices gravida viverra.</p>
  <div class="reason" style="top:272px">
    <svg width="52" height="52" viewBox="0 0 52 52" fill="none" stroke="#111" stroke-width="3"><path d="M26 5 L44 12 V26 C44 37 36 44 26 48 C16 44 8 37 8 26 V12 Z"/><path d="M17 26 L24 33 L36 20"/></svg>
    <div><h4>Communicate Trust</h4><p>Lorem ipsum dolor sit amet, consectetur adipiscing<br>elit, sed do eiusmod tempor incididuntlabo.</p></div>
  </div>
  <div class="reason" style="top:396px">
    <svg width="52" height="52" viewBox="0 0 52 52" fill="none" stroke="#111" stroke-width="3"><circle cx="26" cy="26" r="21"/><path d="M26 13 V26 L35 32"/></svg>
    <div><h4>Dependability</h4><p>Lorem ipsum dolor sit amet, consectetur adipiscing<br>elit, sed do eiusmod tempor incididuntlabo.</p></div>
  </div>
  <div class="reason" style="top:500px">
    <svg width="52" height="52" viewBox="0 0 52 52" fill="none" stroke="#111" stroke-width="3"><path d="M6 30 L16 40 L46 12"/></svg>
    <div><h4>The Value</h4><p>Lorem ipsum dolor sit amet, consectetur adipiscing<br>elit, sed do eiusmod tempor incididuntlabo.</p></div>
  </div>
  <div class="photo framed" style="left:608px;top:92px;width:216px;height:208px;background:linear-gradient(135deg,#2a1c14,#8a5430 55%,#3a2418)" role="img" aria-label="CNC router bit cutting wood"></div>
  <div class="photo framed" style="left:832px;top:72px;width:216px;height:208px;background:linear-gradient(135deg,#3a2618,#b07a48 50%,#5a3a22)" role="img" aria-label="Intricate cut wooden panel pattern"></div>
  <div class="photo framed" style="left:608px;top:320px;width:216px;height:208px;background:linear-gradient(135deg,#4a2e1c,#c08a58 55%,#6a4428)" role="img" aria-label="Laser-cut wooden gear shapes"></div>
  <div class="photo framed" style="left:832px;top:292px;width:216px;height:208px;background:linear-gradient(135deg,#2a1a10,#7a4a2a 50%,#d09a62)" role="img" aria-label="Decorative wood cutouts under warm light"></div>
</section>

<section class="blog">
  <h2 class="heading section-title" style="top:112px">Latest Blog Posts</h2>
  <article class="post" style="left:132px">
    <div class="photo" style="background:linear-gradient(135deg,#1f3a66,#d8a23a 60%,#4a5a70)" role="img" aria-label="Engineer in a hard hat working on metal"></div>
    <p>Lorem ipsum dolor sit amet, consectetur adipis cing elit sed do eius.</p>
    <time>SEP 27 2023</time>
  </article>
  <article class="post" style="left:452px">
    <div class="photo" style="background:linear-gradient(135deg,#4a4a52,#a0a0a8 50%,#c89a6a 75%,#3a3a40)" role="img" aria-label="Laser cutting a metal sheet"></div>
    <p>Lorem ipsum dolor sit amet, consectetur adipis cing elit sed do eius.</p>
    <time>SEP 27 2023</time>
  </article>
  <article class="post" style="left:776px">
    <div class="photo" style="background:linear-gradient(135deg,#2a3038,#d0782a 50%,#5a6470)" role="img" aria-label="Metal lathe throwing sparks"></div>
    <p>Lorem ipsum dolor sit amet, consectetur adipis cing elit sed do eius.</p>
    <time>SEP 27 2023</time>
  </article>
</section>

<section class="contact">
  <h2 class="heading section-title">Contact Us</h2>
  <div class="field" style="left:228px;top:192px;width:232px;height:40px">Name:</div>
  <div class="field" style="left:468px;top:192px;width:244px;height:40px">Email:</div>
  <div class="field" style="left:720px;top:192px;width:248px;height:40px">Phone:</div>
  <div class="field" style="left:228px;top:248px;width:740px;height:120px">Message:</div>
  <div class="btn" style="left:540px;top:352px;width:120px;height:40px;border:1px solid #444">Submit</div>
</section>

<footer class="site-footer">
  <div class="info" style="top:48px">
    <svg width="18" height="22" viewBox="0 0 18 22" fill="#fff"><path d="M9 0a8 8 0 0 0-8 8c0 6 8 14 8 14s8-8 8-14a8 8 0 0 0-8-8zm0 11a3 3 0 1 1 0-6 3 3 0 0 1 0 6z"/></svg>
    <div><strong>Address:</strong>Lorem dumy text 098</div>
  </div>
  <div class="info" style="top:100px">
    <svg width="18" height="14" viewBox="0 0 18 14" fill="#fff"><path d="M0 0h18v14H0z" fill="none" stroke="#fff" stroke-width="2"/><path d="M1 1l8 7 8-7" fill="none" stroke="#fff" stroke-width="2"/></svg>
    <div><strong>Email:</strong>info@northridgecnc.com</div>
  </div>
  <div class="info" style="top:152px">
    <svg width="18" height="18" viewBox="0 0 24 24" fill="#fff"><path d="M6.6 10.8a15 15 0 0 0 6.6 6.6l2.2-2.2c.3-.3.7-.4 1-.2 1.1.4 2.3.6 3.6.6.6 0 1 .4 1 1V20c0 .6-.4 1-1 1A17 17 0 0 1 3 4c0-.6.4-1 1-1h3.5c.6 0 1 .4 1 1 0 1.3.2 2.5.6 3.6.1.3 0 .7-.2 1z"/></svg>
    <div><strong>Phone:</strong>555 xx x0143</div>
  </div>
  <div class="brand"><span class="brand-mark"></span>NORTH RIDGE CNC</div>
  <nav class="foot-links">
    <div>Home</div><div>Services we offer</div><div>Capabilites</div><div>About us</div><div>Contact</div>
  </nav>
  <p class="copyright">©2023 North Ridge CNC. All rights are reserved.</p>
</footer>

</body>
</html>
```